Letterhead in Word Format

We are a small law firm in the Midwest. Our clientele is generally small business owners and companies.

We recently had a complete re-brand with a new logo, new letterhead, business cards, etc. However, the major issue now is that we cannot use the letterhead without physically ordering letterhead. Thus, invoices, and other items cannot be custom drafted.

We require custom letterhead in MICROSOFT WORD format. Our logo will be provided to you. And we will also provide a copy of the letterhead that was prepared.

We would like to see designs that are black and white, sophisticated, elegant, and generally professional. We prefer a traditional design with just a touch of contemporary.

Please do not submit any designs that are not Microsoft Word compatible.

EDIT: Please view the attached letterhead. The design must include the logo, name, address, fax, phone, email, and name of attorney.
Updates

Thank you all for submitting designs. I just wanted to quickly provide some feedback. I saw a few designs that had the logo at the bottom. Because there will be text with margins at 1" all around, it's not practical have the logo at the bottom. Also, designs with blocks of gray or black would cause our printer to bleed black onto the letterhead, so that is not practical as well.

If you have any comments, please feel free to leave me a message. Thank you.

Target Market(s)

Small business owners, companies, real estate investors and developers.

Industry/Entity Type

Small Business

Font styles to use
Script

Requirements
Must have
• Microsoft Word Format

```html
<!DOCTYPE html>
<html lang="en">
<head>
<meta charset="utf-8">
<title>The Harlow Law Firm – Letterhead</title>
<link rel="stylesheet" href="https://fonts.googleapis.com/css2?family=Cinzel:wght@400&family=Gelasio:wght@400;700&family=Libre+Baskerville:wght@400;700&display=swap">
<style>
  :root {
    --paper: #ffffff;
    --ink: #3f3f3f;
    --ink-dark: #1e1e1e;
    --muted: #7a7a7a;
    --faint: #ececec;
    --signature: #d8d8d8;
  }
  * { margin: 0; padding: 0; box-sizing: border-box; }
  html, body { width: 852px; height: 1200px; overflow: hidden; background: var(--paper); }
  .letterhead {
    position: relative;
    width: 852px;
    height: 1200px;
    overflow: hidden;
    background: var(--paper);
    color: var(--ink);
    font-family: "Gelasio", Georgia, serif;
  }
  .firm-name {
    position: absolute;
    left: 99px;
    top: 112px;
    font-family: "Cinzel", serif;
    font-size: 29px;
    letter-spacing: 0.5px;
    color: var(--ink-dark);
    white-space: nowrap;
  }
  .attorney {
    position: absolute;
    right: 86px;
    top: 92px;
    text-align: right;
    font-family: "Libre Baskerville", serif;
    font-size: 9.5px;
    line-height: 14.5px;
    color: var(--ink-dark);
  }
  .attorney-name { letter-spacing: 0.4px; }
  .attorney-title { color: var(--muted); margin-bottom: 14px; }
  .attorney b { font-weight: 700; }
  .date, .recipient, .body-text, .closing, .signer {
    position: absolute;
    left: 111px;
    font-size: 15.6px;
    line-height: 23.2px;
  }
  .date { top: 287px; }
  .recipient { top: 333px; }
  .recipient-name { font-weight: 700; }
  .body-text { top: 424px; width: 656px; }
  .body-text p { text-align: justify; margin-bottom: 23.2px; }
  .closing { top: 851px; }
  .signature {
    position: absolute;
    left: 94px;
    top: 878px;
    width: 170px;
    height: 58px;
  }
  .signer { top: 919px; }
  .footer-mark {
    position: absolute;
    left: 420px;
    top: 1108px;
    font-family: "Cinzel", serif;
    font-size: 38px;
    color: var(--faint);
    white-space: nowrap;
  }
  .footer-contact {
    position: absolute;
    left: 100px;
    top: 1135px;
    font-family: "Libre Baskerville", serif;
    font-size: 9.5px;
    line-height: 16px;
    color: var(--ink-dark);
  }
  .footer-contact b { font-weight: 700; }
  .footer-contact .gap { margin-left: 14px; }
</style>
</head>
<body>
<main class="letterhead">
  <header>
    <div class="firm-name">THE HARLOW LAW FIRM</div>
    <address class="attorney" style="font-style: normal;">
      <div class="attorney-name">MARCUS L. HARLOW</div>
      <div class="attorney-title">Principal Attorney</div>
      <div><b>Phone:</b> (555)318-4720</div>
      <div><b>Fax:</b> (555) 318-4721</div>
      <div><b>Email:</b> office@harlowlawfirm.com</div>
    </address>
  </header>

  <div class="date">January 26, 2014</div>

  <div class="recipient">
    <div class="recipient-name">Daniel Reyes</div>
    <div>General Manager</div>
    <div>Ridge and Vale Corp</div>
  </div>

  <section class="body-text">
    <p>Lorem ipsum dolor sit amet, consectetur adipiscing elit. Donec orci purus, luctus vitae dignissim eu, iaculis sed purus. Vivamus faucibus, ipsum nec aliquet viverra, leo mauris condimentum ligula, sit amet sagittis enim ligula quis arcu. Nam egestas tortor id nisi porttitor mattis. In tortor ante, ultricies in suscipit a, tempus non massa. Vivamus et auctor mi. Fusce vel massa nulla. Phasellus nec eros mauris, et scelerisque orci. Donec malesuada orci vitae nulla accumsan porta a id massa. Quisque accumsan iaculis magna sit amet fringilla. Maecenas consequat, magna eget tincidunt semper, odio nibh rutrum mi, id feugiat ante nisi eu risus. Vestibulum nunc orci, ultricies in mi.</p>
    <p>Quisque scelerisque sagittis nulla at porttitor. Mauris a justo et tellus interdum tristique. Sed id augue vitae urna euismod commodo aliquet a quam. Pellentesque arcu velit, cursus et malesuada ut, rutrum nisi iaculis consequat et diam. Nullam erat sem, rhoncus id ullamcorper vitae, rhoncus et arcu. In ultricies ultricies nulla, ut rutrum nisi iaculis at. Donec eu magna a metus ornare faucibus. Fusce aliquet faucibus ultricies. Morbi semper, est id tincidunt gravida, sem arcu adipiscing lacus, ac bibendum nulla leo eu purus. Quisque nec diam sed risus consectetur a ccumsan quis quis nibh. Vestibulum id purus lorem.</p>
  </section>

  <div class="closing">Ipsum dolor,</div>
  <svg class="signature" role="img" aria-label="Handwritten signature of the sender" viewBox="0 0 170 58">
    <rect x="0" y="0" width="170" height="58" rx="6" fill="var(--signature)" opacity="0.5"/>
  </svg>
  <div class="signer">Thomas Reed Allen</div>

  <footer>
    <div class="footer-mark" aria-hidden="true">THE HARLOW LAW FIRM</div>
    <div class="footer-contact">
      <div><b>Address:</b> 4820 W. Alder Rd., Brookfield, Illinois 60599</div>
      <div><b>Web:</b> www.harlowlawfirm.com <span class="gap"><b>Email:</b> office@harlowlawfirm.com</span></div>
    </div>
  </footer>
</main>
</body>
</html>
```